Logistics Website Design

See website https://kravenfreightglobal.com for theme and color details. Need the site to be re-done and reflect some of the designs shown in this list here: https://pixelvane.com/tags/logistics-company-website

Target Market(s)

Logistics & Transportation

Industry/Entity Type

Logistics and Supply Chain

Coding

Coded - Design and coding required

Number of Pages Required

5+ page

Requirements
Must have
• Colors must match theme of logo. Looking for a sleek, interactive design.

```html
<!DOCTYPE html>
<html lang="en">
<head>
<meta charset="utf-8">
<title>Kraven Freight — Precision in Motion</title>
<link href="https://fonts.googleapis.com/css2?family=Space+Grotesk:wght@400;500;600;700&family=Manrope:wght@400;500;600;700&family=JetBrains+Mono:wght@400;500&display=swap" rel="stylesheet">
<style>
:root{
  --accent:#ff8f66;
  --accent-deep:#e9734a;
  --cream:#ffe7dc;
  --text:#e8d2c7;
  --muted:#a98c7f;
  --bg-header:#2b2520;
  --bg-stats:#24140e;
  --bg-arch:#180d09;
  --bg-dash:#2c1913;
  --bg-cta:#1f110c;
  --bg-foot:#0f0806;
  --card:#2f1d16;
  --line:#3e2820;
  --violet:#d89af0;
}
*{box-sizing:border-box;margin:0;padding:0}
html,body{width:1200px;height:3572px;overflow:hidden;background:var(--bg-arch)}
body{position:relative;font-family:"Manrope",sans-serif;color:var(--text)}
.abs{position:absolute}
.head{font-family:"Space Grotesk",sans-serif;font-weight:700;letter-spacing:-0.02em;text-transform:uppercase}
.label{font-family:"Space Grotesk",sans-serif;text-transform:uppercase;letter-spacing:.12em}

/* header */
.site-header{left:0;top:0;width:1200px;height:114px;background:var(--bg-header);z-index:2}
.brand{left:30px;top:40px;display:flex;align-items:center;gap:10px;font-family:"Space Grotesk",sans-serif;font-weight:700;font-size:20px;color:var(--accent)}
.brand-dot{width:14px;height:14px;border-radius:50%;background:var(--accent)}
.nav a{position:absolute;top:46px;font-family:"Space Grotesk",sans-serif;font-size:12px;font-weight:500;color:#d8c6bd;text-decoration:none;letter-spacing:-.01em}
.nav a.active{color:var(--accent);border-bottom:1px solid var(--accent);padding-bottom:3px}
.btn-command{left:1004px;top:39px;width:165px;height:35px;background:var(--accent);color:#3a150a;border-radius:4px;font-family:"Space Grotesk",sans-serif;font-weight:600;font-size:13px;display:flex;align-items:center;justify-content:center}

/* hero */
.hero{left:0;top:114px;width:1200px;height:618px;overflow:hidden}
.hero-photo{position:absolute;inset:0;background:linear-gradient(100deg,#2f4a4a 0%,#3b4440 30%,#5a4330 55%,#7a5534 75%,#4a3424 100%)}
.hero-shade{position:absolute;inset:0;background:linear-gradient(90deg,rgba(20,14,10,.55) 0%,rgba(20,14,10,.2) 60%,rgba(20,14,10,0) 100%),linear-gradient(180deg,rgba(0,0,0,0) 70%,rgba(30,18,12,.5) 100%)}
.eyebrow{left:90px;top:95px;display:flex;align-items:center;gap:10px;font-size:11px;font-weight:600;color:var(--accent);letter-spacing:.3em}
.eyebrow span{display:block;width:44px;height:1px;background:var(--accent)}
.hero-title{left:88px;top:128px;font-size:121px;line-height:.99;letter-spacing:-.03em}
.hero-title .l1{color:var(--cream);display:block}
.hero-title .l2{color:var(--accent);display:block}
.hero-sub{left:90px;top:385px;font-size:20px;color:#f4e6de}
.btn{height:58px;border-radius:8px;display:flex;align-items:center;justify-content:center;font-family:"Space Grotesk",sans-serif;font-weight:700;font-size:13px;letter-spacing:.14em;text-transform:uppercase}
.btn-primary{left:90px;top:452px;width:226px;background:var(--accent);color:#3a150a;box-shadow:0 6px 22px rgba(255,143,102,.3)}
.btn-ghost{left:340px;top:452px;width:186px;background:rgba(50,40,36,.85);color:#f0e4dd}

/* stats */
.stats{left:0;top:732px;width:1200px;height:422px;background:var(--bg-stats)}
.stat{top:92px;width:237px;height:238px;background:var(--card);border-radius:8px;border-bottom:3px solid #5a3222}
.stat svg{position:absolute;left:30px;top:34px}
.stat .tag{position:absolute;right:30px;top:32px;font-size:9px;color:#8e7266;letter-spacing:.06em;display:flex;align-items:center;gap:6px}
.stat .tag i{width:6px;height:6px;border-radius:50%;background:var(--accent);display:block}
.stat .num{position:absolute;left:30px;top:138px;font-family:"Space Grotesk",sans-serif;font-weight:600;font-size:45px;color:var(--cream);letter-spacing:-.02em}
.stat .cap{position:absolute;left:30px;top:192px;font-size:11px;color:#a3877b;letter-spacing:.1em}

/* architecture */
.arch{left:0;top:1154px;width:1200px;height:947px;background:var(--bg-arch)}
.arch-title{left:90px;top:118px;font-size:45px;line-height:1.02}
.arch-title .l1{color:var(--cream);display:block}
.arch-title .l2{color:var(--accent);display:block}
.arch-text{left:90px;top:232px;width:620px;font-size:17px;line-height:26px;color:#cdb3a7}
.round-btn{top:232px;width:52px;height:52px;border-radius:50%;display:flex;align-items:center;justify-content:center}
.round-prev{left:989px;border:1px solid #4a3026}
.round-next{left:1057px;background:var(--accent)}
.service{top:359px;width:241px;height:468px;border-radius:8px;border:1px solid #2c1a13;overflow:hidden}
.service-photo{position:absolute;inset:0}
.service-body{position:absolute;left:38px;top:200px;right:20px}
.service-body svg{display:block;margin-bottom:38px}
.service h3{font-family:"Space Grotesk",sans-serif;font-weight:700;font-size:19px;line-height:19px;color:var(--cream);text-transform:uppercase}
.service p{margin-top:15px;font-size:13px;line-height:19px;color:#bda397}
.service .link{margin-top:30px;font-family:"Space Grotesk",sans-serif;font-weight:700;font-size:11px;letter-spacing:.14em;color:var(--accent)}

/* dashboard */
.dash{left:0;top:2101px;width:1200px;height:752px;background:var(--bg-dash)}
.panel{left:90px;top:92px;width:1020px;height:570px;border-radius:16px;background:#100806;border:3px solid #100806;overflow:hidden}
.panel-bar{position:absolute;left:0;top:0;width:100%;height:83px;background:#2a1811;display:flex;align-items:center;padding:0 30px;gap:14px}
.panel-bar .dot{width:11px;height:11px;border-radius:50%;background:#ff6f63}
.panel-bar .name{font-family:"Space Grotesk",sans-serif;font-weight:600;font-size:14px;color:var(--cream);letter-spacing:-.02em}
.chip{position:absolute;top:30px;height:22px;padding:0 10px;font-size:9px;font-weight:700;letter-spacing:.08em;display:flex;align-items:center;border-radius:3px}
.chip-node{left:826px;background:#1a0f0b;color:#d8c2b7;border:1px solid #3a2a24}
.chip-stable{left:927px;background:#4a2418;color:var(--accent);border:1px solid #7a3a26}
.engine{left:0;top:86px;width:674px;height:478px;background:#241510}
.engine h2{position:absolute;left:32px;top:32px;font-size:33px;color:var(--accent);font-family:"Space Grotesk",sans-serif;font-weight:600;letter-spacing:-.01em}
.meter{position:absolute;top:89px;width:184px}
.meter span{display:block;font-size:8px;letter-spacing:.1em;color:#a58a7e;text-transform:uppercase}
.meter b{display:block;margin-top:7px;height:4px;border-radius:2px;background:#3a2820;position:relative}
.meter b i{position:absolute;left:0;top:0;height:4px;border-radius:2px}
.globe{position:absolute;left:32px;top:210px;width:612px;height:240px;border-radius:10px;background:radial-gradient(circle at 50% 45%,#3a2219,#2a1913 70%)}
.side{left:677px;top:86px;width:337px;height:478px;background:#241510}
.feed{position:absolute;left:30px;top:32px;width:275px;height:245px;border-radius:8px;background:#2f1c15;padding:24px 24px}
.feed .t{font-family:"Space Grotesk",sans-serif;font-weight:700;font-size:10px;color:var(--cream);display:flex;justify-content:space-between}
.feed .row{display:flex;gap:16px;margin-top:14px;font-family:"JetBrains Mono",monospace;font-size:9.5px;line-height:15px}
.feed .row em{font-style:normal;color:var(--accent);white-space:nowrap}
.feed .row span{color:#c6afa4}
.growth{position:absolute;left:30px;top:302px;width:275px;height:142px;border-radius:8px;background:#2b1812;border:1px solid #5a3224}
.growth .ico{position:absolute;left:23px;top:24px;width:42px;height:40px;border-radius:6px;background:var(--accent);display:flex;align-items:center;justify-content:center}
.growth .sm{position:absolute;left:80px;top:26px;font-size:8px;letter-spacing:.08em;color:#8a6b5f}
.growth .big{position:absolute;left:80px;top:38px;font-family:"Space Grotesk",sans-serif;font-weight:700;font-size:22px;color:var(--accent)}
.growth .export{position:absolute;left:23px;top:82px;width:228px;height:36px;background:var(--accent);border-radius:4px;display:flex;align-items:center;justify-content:center;font-family:"Space Grotesk",sans-serif;font-weight:700;font-size:10px;letter-spacing:.14em;color:#3a150a}

/* cta */
.cta{left:0;top:2853px;width:1200px;height:617px;background:linear-gradient(115deg,#1a0e0a 0%,#1f110c 60%,#2a1710 100%)}
.pill{left:514px;top:122px;width:170px;height:22px;border:1px solid #8a4a32;border-radius:12px;font-size:8.5px;font-weight:700;letter-spacing:.1em;color:var(--accent);display:flex;align-items:center;justify-content:center}
.cta-title{left:0;top:172px;width:1200px;text-align:center;font-size:63px;line-height:67px;letter-spacing:-.03em}
.cta-title .l1{color:var(--cream);display:block}
.cta-title .l2{color:var(--accent);display:block}
.cta-text{left:0;top:338px;width:1200px;text-align:center;font-size:19px;line-height:27px;color:#cdb3a7}
.email{left:294px;top:440px;width:300px;height:53px;background:#000;border-bottom:2px solid #3a2a24;display:flex;align-items:center;padding-left:24px;font-family:"Space Grotesk",sans-serif;font-size:14px;letter-spacing:.12em;color:#4c3a32}
.btn-onboard{left:617px;top:437px;width:287px;height:60px;background:var(--accent);border-radius:8px;display:flex;align-items:center;justify-content:center;font-family:"Space Grotesk",sans-serif;font-weight:700;font-size:14px;letter-spacing:.14em;color:#3a150a;box-shadow:0 8px 26px rgba(255,143,102,.3)}

/* footer */
.site-footer{left:0;top:3470px;width:1200px;height:102px;background:var(--bg-foot)}
.foot-brand{left:46px;top:40px;font-family:"Space Grotesk",sans-serif;font-weight:700;font-size:18px;color:var(--accent)}
.foot-copy{left:198px;top:45px;font-size:11px;letter-spacing:.06em;color:#7a6258}
.foot-links a{position:absolute;top:45px;font-size:11px;letter-spacing:.08em;color:#d6c4bb;text-decoration:none;text-transform:uppercase}
</style>
</head>
<body>

<header class="abs site-header">
  <div class="abs brand"><span class="brand-dot"></span>Kraven Freight</div>
  <nav class="nav">
    <a class="active" href="#" style="left:653px">FLEET</a>
    <a href="#" style="left:717px">GLOBAL HUB</a>
    <a href="#" style="left:818px">TELEMETRY</a>
    <a href="#" style="left:914px">ANALYTICS</a>
  </nav>
  <div class="abs btn-command">COMMAND CENTER</div>
</header>

<section class="abs hero">
  <div class="hero-photo" role="img" aria-label="Photo of stacked shipping containers seen from below against a teal sky"></div>
  <div class="hero-shade"></div>
  <div class="abs eyebrow label"><span></span>Orbital Command Active</div>
  <h1 class="abs hero-title head"><span class="l1">Precision</span><span class="l2">In Motion</span></h1>
  <p class="abs hero-sub">Secure and reliable transportation for all your cargo needs.</p>
  <div class="abs btn btn-primary">Initialize Shipment</div>
  <div class="abs btn btn-ghost">View Network</div>
</section>

<section class="abs stats">
  <div class="abs stat" style="left:90px">
    <svg width="28" height="28" viewBox="0 0 24 24" fill="none" stroke="#ff8f66" stroke-width="2" stroke-linecap="round"><path d="M6 4v11a4 4 0 0 0 8 0V9a4 4 0 0 1 8 0v11"/><circle cx="6" cy="20" r="1.5"/></svg>
    <div class="tag">LIVE SYNC</div>
    <div class="num">12,482</div><div class="cap">ACTIVE ROUTES</div>
  </div>
  <div class="abs stat" style="left:351px">
    <svg width="28" height="28" viewBox="0 0 24 24" fill="none" stroke="#ff8f66" stroke-width="2"><rect x="10" y="3" width="11" height="8" rx="1"/><path d="M7 7v7h11"/><path d="M3 11v7h11"/></svg>
    <div class="tag"><i></i>REALTIME</div>
    <div class="num">99.9%</div><div class="cap">FLEET TELEMETRY</div>
  </div>
  <div class="abs stat" style="left:612px">
    <svg width="30" height="30" viewBox="0 0 24 24" fill="none" stroke="#ff8f66" stroke-width="1.8"><circle cx="12" cy="12" r="3"/><circle cx="12" cy="3" r="1.6"/><circle cx="12" cy="21" r="1.6"/><circle cx="3.5" cy="8" r="1.6"/><circle cx="20.5" cy="8" r="1.6"/><circle cx="3.5" cy="16" r="1.6"/><circle cx="20.5" cy="16" r="1.6"/><path d="M12 5v4M12 15v4M5 9l4 2M19 9l-4 2M5 15l4-2M19 15l-4-2"/></svg>
    <div class="tag">GLOBAL EDGE</div>
    <div class="num">240</div><div class="cap">GLOBAL HUBS</div>
  </div>
  <div class="abs stat" style="left:872px">
    <svg width="28" height="28" viewBox="0 0 24 24" fill="none" stroke="#ff8f66" stroke-width="2" stroke-linejoin="round"><path d="M13 2 4 14h7l-1 8 9-12h-7z"/></svg>
    <div class="tag">PROTOCOL 4</div>
    <div class="num">100%</div><div class="cap">SYSTEM UPTIME</div>
  </div>
</section>

<section class="abs arch">
  <h2 class="abs arch-title head"><span class="l1">Omni-Channel</span><span class="l2">Logistics Architecture</span></h2>
  <p class="abs arch-text">Our multi-modal infrastructure ensures seamless cargo transition across any atmospheric or oceanic corridor.</p>
  <div class="abs round-btn round-prev"><svg width="18" height="18" viewBox="0 0 24 24" fill="none" stroke="#e8d2c7" stroke-width="2"><path d="M19 12H5M11 6l-6 6 6 6"/></svg></div>
  <div class="abs round-btn round-next"><svg width="18" height="18" viewBox="0 0 24 24" fill="none" stroke="#3a150a" stroke-width="2"><path d="M5 12h14M13 6l6 6-6 6"/></svg></div>

  <article class="abs service" style="left:90px">
    <div class="service-photo" role="img" aria-label="Dim photo of a flatbed truck at an airfield" style="background:linear-gradient(180deg,#1f130e 0%,#2c1c15 45%,#2a1811 65%,#160c08 100%)"></div>
    <div class="service-body">
      <svg width="64" height="48" viewBox="0 0 64 48" fill="none" stroke="#fff" stroke-width="2"><path d="M4 34h36V24H4zM40 34V18h10l8 9v7H40"/><circle cx="14" cy="38" r="4" fill="#fff"/><circle cx="50" cy="38" r="4" fill="#fff"/></svg>
      <h3>Flatbed<br>Transportation</h3>
      <p>From routine shipments to oversized and heavy-haul loads, we handle...</p>
      <div class="link">CONFIGURE ROUTE →</div>
    </div>
  </article>
  <article class="abs service" style="left:351px">
    <div class="service-photo" role="img" aria-label="Dim photo of a port with cranes and a step deck truck" style="background:linear-gradient(180deg,#1f130e 0%,#2e1d16 45%,#2b1812 65%,#160c08 100%)"></div>
    <div class="service-body">
      <svg width="64" height="48" viewBox="0 0 64 48" fill="none" stroke="#fff" stroke-width="2"><path d="M6 34h30V26h8V16h10l6 8v10H6"/><circle cx="16" cy="38" r="4" fill="#fff"/><circle cx="50" cy="38" r="4" fill="#fff"/></svg>
      <h3>Step Deck<br>Transportation</h3>
      <p>Our step deck trucking services support tall, heavy, and specialized...</p>
      <div class="link">CONFIGURE ROUTE →</div>
    </div>
  </article>
  <article class="abs service" style="left:612px">
    <div class="service-photo" role="img" aria-label="Dim photo of a dry van truck on a road" style="background:linear-gradient(180deg,#3a2016 0%,#3a2218 40%,#2c1810 65%,#170c08 100%)"></div>
    <div class="service-body">
      <svg width="64" height="48" viewBox="0 0 64 48" fill="none" stroke="#fff" stroke-width="2"><path d="M4 10h38v24H4zM42 18h10l8 9v7H42"/><circle cx="14" cy="38" r="4" fill="#fff"/><circle cx="52" cy="38" r="4" fill="#fff"/></svg>
      <h3>Dry Van<br>Transportation</h3>
      <p>From consumer goods to industrial materials, our dry van services provide the...</p>
      <div class="link">CONFIGURE ROUTE →</div>
    </div>
  </article>
  <article class="abs service" style="left:872px">
    <div class="service-photo" role="img" aria-label="Dim photo of a heavy haul tanker truck beside containers" style="background:linear-gradient(180deg,#261812 0%,#2e1d16 45%,#2a1811 65%,#160c08 100%)"></div>
    <div class="service-body">
      <svg width="64" height="48" viewBox="0 0 64 48" fill="none" stroke="#fff" stroke-width="2"><rect x="4" y="14" width="36" height="18" rx="9"/><path d="M40 16h10l8 9v9H4"/><circle cx="14" cy="38" r="4" fill="#fff"/><circle cx="50" cy="38" r="4" fill="#fff"/></svg>
      <h3>Heavy Haul<br>Transportation</h3>
      <p>We provide heavy haul trucking solutions for oversized, overweight...</p>
      <div class="link">CONFIGURE ROUTE →</div>
    </div>
  </article>
</section>

<section class="abs dash">
  <div class="abs panel">
    <div class="panel-bar"><span class="dot"></span><span class="name">LIVE COMMAND DASHBOARD</span></div>
    <div class="chip chip-node">NODE: 0X42F</div>
    <div class="chip chip-stable">STABLE</div>
    <div class="abs engine">
      <h2>ANALYTICS ENGINE v.2.04</h2>
      <div class="meter" style="left:32px"><span>Efficiency</span><b><i style="width:88%;background:var(--accent)"></i></b></div>
      <div class="meter" style="left:246px"><span>Saturation</span><b><i style="width:63%;background:var(--violet)"></i></b></div>
      <div class="meter" style="left:460px"><span>Latency</span><b><i style="width:12%;background:#f6e6dc"></i></b></div>
      <div class="globe">
        <svg style="position:absolute;left:256px;top:70px" width="100" height="100" viewBox="0 0 24 24" fill="none" stroke="#5a3a2e" stroke-width="2"><circle cx="12" cy="12" r="10"/><path d="M2 12h20M12 2c3 3 3 17 0 20M12 2c-3 3-3 17 0 20"/></svg>
      </div>
    </div>
    <div class="abs side">
      <div class="feed">
        <div class="t"><span>TERMINAL FEED</span><span style="color:#8a6b5f">···</span></div>
        <div class="row"><em>[14:22:01]</em><span>HUB_CENTRAL: Connection established.</span></div>
        <div class="row"><em>[14:22:05]</em><span>FLT_882: Deploying to Sector G-7.</span></div>
        <div class="row"><em>[14:22:12]</em><span>SYS: Optimizing delivery vectors...</span></div>
        <div class="row"><em>[14:22:18]</em><span style="color:var(--accent)">KPI: Efficiency reached +4.2%</span></div>
      </div>
      <div class="growth">
        <div class="ico"><svg width="20" height="20" viewBox="0 0 24 24" fill="none" stroke="#3a150a" stroke-width="2"><path d="M3 14l5-5 4 4 6-6"/><circle cx="16" cy="16" r="3"/><path d="M18 18l3 3"/></svg></div>
        <div class="sm">PROJECTED GROWTH</div>
        <div class="big">+$1.2M</div>
        <div class="export">EXPORT DATA</div>
      </div>
    </div>
  </div>
</section>

<section class="abs cta">
  <div class="abs pill">SECURE GLOBAL TERMINAL</div>
  <h2 class="abs cta-title head"><span class="l1">Ready to upgrade your</span><span class="l2">Supply Chain DNA?</span></h2>
  <p class="abs cta-text">Join the network of top-tier industrial leaders leveraging the kinetic<br>archive for absolute supply chain dominance.</p>
  <div class="abs email">ENTER TERMINAL EMAIL</div>
  <div class="abs btn-onboard">INITIALIZE ONBOARDING</div>
</section>

<footer class="abs site-footer">
  <div class="abs foot-brand">KRAVEN FREIGHT</div>
  <div class="abs foot-copy">© 2026. AN INDEPENDENT AGENT OF HALVERN GROUP LLC.</div>
  <nav class="foot-links">
    <a href="#" style="left:703px">Manifesto</a>
    <a href="#" style="left:804px">Safety Protocols</a>
    <a href="#" style="left:958px">Terminal Access</a>
    <a href="#" style="left:1103px">Privacy</a>
  </nav>
</footer>

</body>
</html>
```